Harbor Lights Fade

We need a book cover for our novel. It is a sports story about an athlete who suffers a brain injury on the football field. Please go to www.thefilmharborlightsfade.com to see the trailer for the film. Please disregard the still photo on the website as that is not our vision for the cover. Time is of the essence.

```html
<!DOCTYPE html>
<html lang="en">
<head>
<meta charset="utf-8">
<title>Harbor Lights Fade — Book Cover</title>
<link rel="stylesheet" href="https://fonts.googleapis.com/css2?family=Catamaran:wght@400;500&family=Cinzel:wght@400;500&display=swap">
<style>
  :root {
    --teal-deep: #3f8a9c;
    --teal-mid: #6aa9b3;
    --sand: #c9b57a;
    --ochre: #b39a4f;
    --spine-top: #a9d6dc;
    --spine-bottom: #efe8bf;
    --crimson: #b8174a;
    --ink: #1d1d1d;
    --rule: #8f9597;
    --white: #ffffff;
  }
  * { margin: 0; padding: 0; box-sizing: border-box; }
  html, body { width: 1200px; height: 900px; overflow: hidden; background: #fff; }
  .cover {
    position: relative;
    width: 1200px;
    height: 900px;
    overflow: hidden;
    font-family: "Catamaran", "Helvetica Neue", Arial, sans-serif;
  }

  /* Back cover */
  .back-cover {
    position: absolute; left: 0; top: 0; width: 540px; height: 900px;
    background:
      radial-gradient(ellipse at 20% 15%, rgba(255,255,255,0.12), transparent 55%),
      linear-gradient(180deg, var(--teal-deep) 0%, var(--teal-mid) 28%, #9fbfb0 48%, var(--sand) 66%, var(--ochre) 100%);
    color: var(--ink);
    text-align: center;
  }
  .back-blurb {
    position: absolute; left: 20px; width: 500px; top: 124px;
    font-size: 17px; line-height: 29px;
  }
  .author-profile { position: absolute; left: 20px; width: 516px; top: 570px; }
  .author-profile h2 {
    font-weight: 400; font-size: 16px; letter-spacing: 0.2px; margin-bottom: 10px;
  }
  .author-profile p { font-size: 17px; line-height: 29px; }

  /* Spine */
  .spine {
    position: absolute; left: 540px; top: 0; width: 92px; height: 900px;
    background: linear-gradient(180deg, var(--spine-top) 0%, #cfe6df 50%, var(--spine-bottom) 100%);
  }
  .spine-title {
    position: absolute; left: 50%; top: 140px;
    transform-origin: 0 0;
    transform: rotate(90deg) translateY(-50%);
    white-space: nowrap;
    font-family: "Cinzel", "Times New Roman", serif;
    font-size: 50px; line-height: 1; letter-spacing: 2px;
    color: var(--crimson);
  }
  .spine-author {
    position: absolute; left: 0; width: 92px; top: 796px;
    text-align: center;
    font-family: "Cinzel", "Times New Roman", serif;
    font-size: 15px; line-height: 22px; letter-spacing: 0.5px;
    color: var(--white);
    text-shadow: 0 0 2px #222, 0 0 1px #222;
  }

  /* Front cover */
  .front-cover { position: absolute; left: 632px; top: 0; width: 568px; height: 900px; }
  .front-photo {
    position: absolute; inset: 0;
    background:
      radial-gradient(ellipse at 45% 55%, rgba(220,222,210,0.55), transparent 45%),
      linear-gradient(180deg, #2d3a3a 0%, #6f9ea5 22%, #8fbcc0 38%, #4a5650 58%, #7c7f6c 78%, #2f3528 100%);
  }
  .front-title {
    position: absolute; left: 52px; top: 66px; width: 510px;
    font-family: "Cinzel", "Times New Roman", serif;
    font-weight: 400; font-size: 92px; line-height: 82px;
    color: var(--crimson);
  }
  .title-rule {
    position: absolute; left: 22px; top: 312px; width: 546px; height: 2px;
    background: var(--rule);
  }
  .front-author {
    position: absolute; left: 94px; top: 812px;
    font-family: "Cinzel", "Times New Roman", serif;
    font-size: 38px; letter-spacing: 3px; color: var(--white);
    white-space: nowrap;
  }
  .front-author .by { font-size: 26px; margin-right: 8px; }
</style>
</head>
<body>
<div class="cover">
  <section class="back-cover">
    <p class="back-blurb">
      We need a book cover for our novel. It is a sports story about an<br>
      athlete who suffers a brain injury on the football field. Please go to<br>
      www.thefilmharborlightsfade.com to see the trailer for the film.<br>
      Please disregard the still photo on the website as that is not our vision<br>
      for the cover. Time is of the essence.
    </p>
    <div class="author-profile">
      <h2>AUTHOR’S PROFILE</h2>
      <p>
        We need a book cover for our novel. It is a sports story about an<br>
        athlete who suffers a brain injury on the football field. Please go to<br>
        www.thefilmharborlightsfade.com to see the trailer for the film.
      </p>
    </div>
  </section>

  <section class="spine">
    <div class="spine-title">Harbor Lights Fade</div>
    <div class="spine-author">BY<br>AUTHOR’S<br>NAME</div>
  </section>

  <section class="front-cover">
    <div class="front-photo" role="img" aria-label="Toned photograph of a football player mid-kick, cleat sole toward the viewer, stadium stand behind"></div>
    <h1 class="front-title">Harbor<br>Lights<br>Fade</h1>
    <div class="title-rule"></div>
    <p class="front-author"><span class="by">BY</span>AUTHOR’S NAME</p>
  </section>
</div>
</body>
</html>
```